Nine Rung Ledger Remedy Seminar

I would like a flyer to hand out to participants at the speeches that we give. We are a CPA firm that specializes in entrepreneurs and realtors. We would like a flyer that looks crisp and clean, that integrates our logo and our company colors (shades of blue & gold). We would like the wording to be as laid out in the attached documents, but design is up to you. We would like a picture to go along with each point and are open to ideas. The flyer should be one page, preferably just the front.

Colors
3176b5
fee18a

Requirements
Must have
• Our logo and the wording supplied.
• A picture to go along with each topic.
Nice to have
• Images that pop, clean look, professional.
Should not have
• Look messy.

```html
<!DOCTYPE html>
<html lang="en">
<head>
<meta charset="utf-8">
<title>Nine Rung Ledger Remedy Seminar Agenda</title>
<link href="https://fonts.googleapis.com/css2?family=PT+Sans+Narrow:wght@700&family=Source+Sans+3:ital,wght@0,400;0,600;0,700;1,400&family=Libre+Caslon+Text:ital@1&display=swap" rel="stylesheet">
<style>
  :root {
    --blue: #3176b5;
    --blue-deep: #2a5a9c;
    --blue-dark: #1f4a86;
    --navy: #1d3f7a;
    --gold: #fee18a;
    --gold-dark: #b8893a;
    --gold-mid: #d4a954;
    --ink: #4a4a4a;
    --paper: #ffffff;
    --backdrop: #d9d9d9;
  }
  * { box-sizing: border-box; margin: 0; padding: 0; }
  html, body { width: 1200px; height: 960px; overflow: hidden; }
  body {
    background: var(--backdrop);
    font-family: "Source Sans 3", sans-serif;
    color: var(--ink);
  }
  .flyer {
    position: absolute;
    left: 252px; top: 30px;
    width: 696px; height: 900px;
    background: var(--paper);
    box-shadow: 0 10px 30px rgba(0,0,0,.18);
    overflow: hidden;
  }
  .side-panel {
    position: absolute; left: 0; top: 0;
    width: 290px; height: 900px;
    background: linear-gradient(180deg, var(--blue-deep) 0%, var(--blue) 45%, var(--blue-dark) 100%);
  }
  .side-photo {
    position: absolute; left: 0; top: 330px;
    width: 290px; height: 370px;
    background: radial-gradient(ellipse at 45% 55%, rgba(20,40,90,.45) 0%, rgba(49,118,181,0) 65%);
  }
  .title {
    position: absolute; left: 24px; top: 104px; width: 260px;
    font-family: "PT Sans Narrow", sans-serif; font-weight: 700;
    font-size: 46px; line-height: 1.12; color: #fff;
    text-shadow: 0 2px 3px rgba(0,0,0,.25);
  }
  .motto {
    position: absolute; left: 34px; top: 556px;
    font-size: 21px; line-height: 1.3; font-style: italic; color: #fff;
  }
  .about {
    position: absolute; left: 24px; top: 776px; width: 230px;
    font-size: 9.5px; line-height: 1.35; color: #dfe8f5;
  }
  .brand {
    position: absolute; right: 28px; top: 26px; text-align: right;
  }
  .brand-name {
    display: flex; align-items: center; justify-content: flex-end; gap: 10px;
    font-weight: 700; font-size: 36px; color: var(--navy); letter-spacing: -.5px;
  }
  .brand-mark { width: 16px; height: 16px; background: var(--gold-dark); }
  .brand-sub {
    margin-top: 8px;
    font-family: "Libre Caslon Text", serif; font-style: italic;
    font-size: 11.5px; color: #222;
  }
  .agenda {
    position: absolute; left: 308px; top: 138px; width: 362px;
    list-style: none;
  }
  .agenda li {
    display: flex; gap: 10px; margin-bottom: 15px;
    font-size: 12.5px; line-height: 1.28; text-align: justify;
  }
  .step-num {
    flex: 0 0 26px; height: 26px; border-radius: 3px;
    background: var(--navy); color: #fff;
    font-weight: 700; font-size: 15px;
    display: flex; align-items: center; justify-content: center;
    margin-top: 2px;
  }
  .slogan-band {
    position: absolute; left: 0; top: 706px; width: 696px; height: 44px;
    background: linear-gradient(90deg, var(--gold-mid) 0%, var(--gold-dark) 55%, #a97b30 100%);
    color: #fff; font-size: 19px;
    display: flex; align-items: center; padding-left: 26px;
  }
  .contact {
    position: absolute; left: 290px; top: 772px; width: 406px;
    text-align: center; font-size: 11px; line-height: 1.5; color: #333;
  }
  .contact-row { display: flex; justify-content: space-around; }
</style>
</head>
<body>
  <article class="flyer">
    <aside class="side-panel">
      <div class="side-photo" role="img" aria-label="Photo of a person relaxing in a lounge chair by the sea, tinted blue"></div>
      <h1 class="title">Nine Rung Ledger Remedy Seminar Agenda</h1>
      <p class="motto">Less Tax.<br>More Fun.<br>Keelbrook Figures.</p>
      <p class="about">We are a full-service Accounting firm licensed in CA. We offer a broad range of services for business owners, executives, and independent professionals. We are affordable, experienced, and friendly.</p>
    </aside>

    <header class="brand">
      <div class="brand-name"><span class="brand-mark"></span>Keelbrook Figures</div>
      <p class="brand-sub">A Professional Accounting Corporation</p>
    </header>

    <ol class="agenda">
      <li><span class="step-num">1.</span><p>We will first show you how to eliminate much of your self-employment tax on your return by converting your business into an S Corporation. A business owner making over $120,000 per year can save about $12,000 per year by doing this.</p></li>
      <li><span class="step-num">2.</span><p>We will show you how to get tax free income from your corporation by renting you home to the corporation for the board meetings. Many of our clients are getting up to $21,000 in tax free income which could put $8,400 cash into your pocket.</p></li>
      <li><span class="step-num">3.</span><p>We will show you the easiest way to track your expenses so that the only thing you will have to do to have rock solid books is to take a picture of the receipt and throw it away. It doesn't get any better than that.</p></li>
      <li><span class="step-num">4.</span><p>Next, we show you the importance of tax planning and why it is critical to meet with your CPA before the end of the year and not just when you do your tax preparation.</p></li>
      <li><span class="step-num">5.</span><p>We will show you how to hire your children and get $7,500 per child tax free. This will save you $3,000 per child in income tax reduction.</p></li>
      <li><span class="step-num">6.</span><p>We will discuss how to make your child's college education tax deductible. With college cost spiraling out of control this is a biggie. Most of our clients have a savings of about $12,000 per year of college.</p></li>
      <li><span class="step-num">7.</span><p>Our grand finale is to show you how to use, not one, but two corporations to get a several hundred thousand dollar tax deferral, get an interest free loan from the government and use that money to grow your business and your wealth.</p></li>
    </ol>

    <div class="slogan-band">If they drive by with a machine gun you don't have to stand up.</div>

    <address class="contact" style="font-style:normal">
      <div>Keelbrook Figures, A Professional Accounting Corporation</div>
      <div>2210 Orchard Row, Ste. B, Larkvale, CA 95000</div>
      <div class="contact-row"><span>Phone: 555-010-4420</span><span>Fax: 555-010-4421</span></div>
      <div class="contact-row"><span>dana@keelbrookfigures.com</span><span>owen@keelbrookfigures.com</span></div>
      <div>www.keelbrookfigures.com</div>
    </address>
  </article>
</body>
</html>
```